Proposal Document Template for New Accounting and Tax Clients

Hi Tarek,
We hope you are well.
We are an Accounting Firm based in the suburb of Pyrmont near Sydney city, and you recently designed a Package Title page for us that we use when providing our clients their year end statements and tax returns.

Because we like the design so much, we would like to work with you again. We would like you to incorporate aspects of your original Package Title Page design throughout our Proposal Document to provide design consistency between both documents.

We need our Proposal Document to be a fully editable Word document, as we send it to potential new clients to win their business and we will need to adjust what we include to suit each one.

We also think it could work if the design includes key images from our website.

We have two key brand colours:
Blue - Hex code #021738
Gold - Hex code #b2a98c

I have included:
- New Thornvale Advisory Title Page_050225 - this was your previous design that we would like the Proposal Document to look similar to
- Proposal Document_V2_Detailed_Owen - this is our current Proposal Document that we would like you to redesign, keeping the content, but updating the design to look consistent with the New Thornvale Advisory Title Page.
- Our Logo in different colours in JPEG Format (I also have PNG and EPS files of these. If you need them, please let me know)
- The key images from our website www.thornvale.net.au

Please let me know if you have any questions or need anything further.

Thank you in advance
Jo
Updates

We received the designs one day ago, that combined with the Easter Holiday break means we need more time to review and provide feedback.

Target Market(s)

Accounting, Tax, and Strategic Business Planning Clients from Small Business, to Corporates , and Individuals

Industry/Entity Type

Accounting

Font styles to use
Other font styles liked:
• Calibri

Requirements
Must have
• Our logo and the ability to edit the document
Nice to have
• Include images from our website thornvale.net.au

```html
<!DOCTYPE html>
<html lang="en">
<head>
<meta charset="utf-8">
<title>Thornvale Advisory – Services Proposal</title>
<link rel="stylesheet" href="https://fonts.googleapis.com/css2?family=Carlito:ital,wght@0,400;0,700;1,400&display=swap">
<style>
:root{
  --navy:#021738;
  --gold:#b2a98c;
  --board:#a9b8d1;
  --paper:#ffffff;
  --cream:#f5f4f1;
  --ink:#1d1d1f;
}
*{box-sizing:border-box;margin:0;padding:0}
html,body{width:906px;height:1200px;overflow:hidden}
body{background:var(--board);font-family:"Carlito",Calibri,sans-serif;color:var(--ink);position:relative}
h1,h2,h3,h4{font-weight:400}
.page{position:absolute;width:259px;height:366px;overflow:hidden;background:var(--paper)}
.abs{position:absolute}
.shapes{position:absolute;inset:0;width:100%;height:100%}
.photo{position:absolute}

/* plain wordmark: one colour, one weight, one square */
.wordmark{display:flex;align-items:center;gap:4px;white-space:nowrap;font-weight:400;line-height:1;color:var(--navy)}
.wordmark .mark{display:inline-block;width:.7em;height:.7em;background:currentColor}
.wordmark.light{color:#fff}

.small{font-size:4px;line-height:5.9px}
ul.dash{list-style:none}
ul.dash li{padding-left:8px;position:relative}
ul.dash li::before{content:"-";position:absolute;left:0}

/* page positions */
.p-cover{left:45px;top:36px}
.p-about{left:324px;top:36px;background:#f3f3f4}
.p-team{left:603px;top:36px}
.p-intro{left:45px;top:418px;background:#f2f2f3}
.p-letter{left:324px;top:418px}
.p-fees{left:603px;top:418px}
.p-closing{left:45px;top:801px}
.p-accept{left:324px;top:801px;background:var(--cream)}

/* cover */
.cover-title{left:20px;top:114px;font-size:17.5px;font-weight:700;color:var(--navy);line-height:1.02;letter-spacing:.3px}
.cover-rule{left:19px;top:300px;width:48px;height:1.5px;background:var(--gold)}
.cover-contact{left:20px;top:308px;color:#fff;font-size:5.6px;line-height:7.5px}
.cover-address{left:20px;top:330px;color:#fff;font-size:3.2px;line-height:5.5px}
.cover-date{left:203px;top:322px;color:#fff;text-align:center;line-height:1}
.cover-date .day{font-size:8.5px;display:block}
.cover-date .year{font-size:13.5px;display:block;margin-top:5px}

/* about */
.about-kicker{left:37px;top:70px;font-size:18px;color:var(--gold);letter-spacing:.8px}
.about-title{left:37px;top:97px;font-size:18.5px;font-weight:700;color:var(--navy);line-height:1.4;letter-spacing:.4px}
.about-rule{left:37px;top:154px;width:45px;height:2px;background:var(--gold)}
.about-body{left:37px;top:174px;width:186px;font-size:6.1px;line-height:8.5px;font-weight:700;color:#222;text-align:justify}
.about-body p{margin-bottom:4.4px}

/* team */
.team-title{left:24px;top:35px;font-size:18px;color:var(--gold);letter-spacing:.4px;font-weight:400}
.team-title b{font-weight:700}
.member{position:absolute;width:63px}
.member .portrait{width:63px;height:62px;background:linear-gradient(#d7d7d7,#a7a7a7);border:1.5px solid var(--navy)}
.member .tag{height:12px;font-size:3.6px;color:#fff;text-align:center;line-height:12px;letter-spacing:.2px}
.tag.navy{background:var(--navy)}
.tag.gold{background:var(--gold)}
.team-brand{left:130px;top:186px;transform:translateX(-50%);font-size:7.5px}

/* intro */
.intro-kicker{left:24px;top:33px;font-size:10.5px;color:var(--navy);letter-spacing:.3px}
.intro-title{left:24px;top:48px;font-size:15.5px;font-weight:700;color:var(--navy);line-height:21px;letter-spacing:.3px}
.intro-meta{left:24px;top:101px;width:215px;color:var(--navy)}
.intro-meta .lab{font-size:7.5px;letter-spacing:.3px}
.intro-meta .client{font-size:8px;font-weight:700;margin:5px 0 7px}
.intro-meta .by{font-size:5px;margin-bottom:5px}
.intro-meta .who{font-size:5.8px;margin-bottom:6px}
.intro-meta .note{font-size:4px;line-height:5.6px;color:#333}
.head-card{position:absolute;width:46px}
.head-card .portrait{height:46px;background:linear-gradient(#e0e0e0,#9e9e9e);border:1.5px solid var(--navy);border-bottom:none}
.head-card .tag{height:8px;background:var(--navy);color:#fff;font-size:3px;text-align:center;line-height:8px}
.head-bio{position:absolute;width:88px;font-size:4px;line-height:6.6px;color:#333}
.head-bio h4{font-size:4px;font-weight:700;color:var(--navy);line-height:6.6px;margin-bottom:3px}
.head-bio p{margin-bottom:3px}

/* letter */
.letter-rule{left:99px;top:47px;width:136px;height:1px;background:var(--gold)}
.letter-body{left:23px;top:64px;width:214px;color:#333}
.letter-body p{margin-bottom:5.9px}

/* fees */
.fees-body{left:24px;top:44px;width:212px;color:#333}
table{border-collapse:collapse;width:100%;font-size:3.9px;line-height:5.2px}
.fee-table th{background:var(--gold);color:var(--navy);font-weight:700;text-align:left;padding:1px 2px;vertical-align:top}
.fee-table td{border:.5px solid #c9c3b0;padding:0 2px;vertical-align:top}
.fee-table .num{text-align:right}
.fee-table .gap td{height:5.9px}
.fee-table .total td{font-weight:700}
.rate-table th{background:var(--gold);color:var(--navy);font-weight:700;text-align:left;padding:2.5px 2px}
.rate-table td{border:.5px solid #c9c3b0;padding:3.4px 2px}
.rate-table .num{text-align:right}
.fees-body p{margin:5px 0}

/* closing */
.closing-body{left:24px;top:41px;width:215px;color:#333}
.closing-body p{margin-bottom:5.9px}
.closing-sign{margin-top:42px}

/* acceptance */
.accept-body{left:29px;top:43px;width:205px;color:#333}
.accept-body h3{font-size:6px;font-weight:700;color:var(--navy);margin-bottom:5px}
.accept-list{display:grid;grid-template-columns:111px 10px;font-size:4px;line-height:6.2px;margin-left:2px}
.accept-list .hd{font-weight:700;color:var(--navy);margin-bottom:5px}
.box{display:inline-block;width:3.6px;height:3.6px;border:.5px solid #444;margin-top:1.2px}
.sign-grid{display:grid;grid-template-columns:33px 82px 60px;font-size:4px;line-height:6px;margin-left:2px;margin-top:27px;row-gap:4px}
.dots{border-bottom:.6px dotted #555;height:4px;margin-right:20px}
.liability{left:27px;top:319px;color:#fff;font-size:4px;line-height:6.6px}
.accept-brand{right:14px;top:338px;font-size:7px}
</style>
</head>
<body>

<!-- 1 · Cover -->
<section class="page p-cover">
  <div class="photo" style="inset:0;background:linear-gradient(160deg,#cfc6bb 0%,#b9aa99 35%,#8c8a88 60%,#4a5058 85%)" role="img" aria-label="Photo of a harbour landmark roof against a cloudy sky"></div>
  <svg class="shapes" viewBox="0 0 259 366" preserveAspectRatio="none">
    <polygon points="205,0 259,0 259,70" fill="var(--navy)"/>
    <polygon points="0,220 216,366 0,366" fill="#fff"/>
    <polygon points="0,232 198,366 0,366" fill="var(--navy)"/>
    <polygon points="259,234 259,366 140,366" fill="#fff"/>
    <polygon points="259,246 259,366 158,366" fill="var(--gold)"/>
  </svg>
  <div class="abs wordmark" style="left:21px;top:22px;font-size:9px"><span class="mark"></span>Thornvale Advisory</div>
  <h1 class="abs cover-title">SERVICES<br>PROPOSAL</h1>
  <div class="abs cover-rule"></div>
  <div class="abs cover-contact">+612 9000 4100<br>thornvale.net.au</div>
  <div class="abs cover-address">Level 3, Suite 4<br>18 Harbour Lane<br>Pyrmont NSW 2009</div>
  <div class="abs cover-date"><span class="day">7 January</span><span class="year">2025</span></div>
</section>

<!-- 2 · About -->
<section class="page p-about">
  <div class="photo" style="inset:0;background:linear-gradient(135deg,#f6f6f7 0%,#ececed 45%,#dcdcdd 100%)" role="img" aria-label="Faded photo of a cable-stayed bridge"></div>
  <div class="abs about-kicker">ABOUT</div>
  <h2 class="abs about-title">THORNVALE<br>ADVISORY</h2>
  <div class="abs about-rule"></div>
  <div class="abs about-body">
    <p>We are a boutique professional services firm focused on delivering customised accounting, tax and strategic business advice for our clients.</p>
    <p>We use our extensive chartered accounting and specialist tax experience to make your life easier by providing clear and concise advice on complex tax matters and business management.</p>
    <p>We pride ourselves on bringing life to numbers.</p>
    <p>We are trusted advisors to small-to-medium enterprises (SMEs), Australian Securities Exchange (ASX) listed companies, local branches of significant global entities (SGEs), technology startups, and high net worth individuals (HNWI).</p>
  </div>
</section>

<!-- 3 · Team -->
<section class="page p-team">
  <div class="photo" style="left:0;top:0;width:259px;height:150px;background:linear-gradient(#e9e9ea,#f7f7f7 70%,#fff)" role="img" aria-label="Faded group photo of the team"></div>
  <h2 class="abs team-title">OUR <b>TEAM</b></h2>
  <svg class="shapes" viewBox="0 0 259 366" preserveAspectRatio="none">
    <polygon points="162,80 194,62 194,150 162,150" fill="var(--navy)"/>
    <polygon points="70,192 130,132 190,192 130,252" fill="var(--navy)"/>
    <polygon points="26,255 90,255 130,282 26,282" fill="var(--gold)"/>
    <polygon points="163,255 235,255 212,282 163,282" fill="var(--gold)"/>
    <polygon points="101,84 101,80 162,80 162,84" fill="var(--gold)"/>
  </svg>
  <div class="member" style="left:26px;top:106px"><div class="portrait" role="img" aria-label="Portrait of Owen Harcourt"></div><div class="tag gold">OWEN HARCOURT</div></div>
  <div class="member" style="left:101px;top:84px"><div class="portrait" role="img" aria-label="Portrait of Clara Venti"></div><div class="tag navy">CLARA VENTI</div></div>
  <div class="member" style="left:173px;top:106px"><div class="portrait" role="img" aria-label="Portrait of Marcus Ellery"></div><div class="tag gold">MARCUS ELLERY</div></div>
  <div class="member" style="left:26px;top:192px"><div class="portrait" role="img" aria-label="Portrait of Priya Ramanathan"></div><div class="tag navy">PRIYA RAMANATHAN</div></div>
  <div class="member" style="left:173px;top:192px"><div class="portrait" role="img" aria-label="Portrait of Sophie Arden"></div><div class="tag navy">SOPHIE ARDEN</div></div>
  <div class="member" style="left:101px;top:227px"><div class="portrait" role="img" aria-label="Portrait of Graham Tolley"></div><div class="tag gold">GRAHAM TOLLEY</div></div>
  <div class="abs wordmark light team-brand"><span class="mark"></span>Thornvale Advisory</div>
</section>

<!-- 4 · Proposal intro -->
<section class="page p-intro">
  <div class="photo" style="left:0;top:60px;width:259px;height:200px;background:linear-gradient(#f2f2f3,#d9dbe0 45%,#e8e9ec 80%,#f2f2f3)" role="img" aria-label="Faded city skyline photo"></div>
  <svg class="shapes" viewBox="0 0 259 366" preserveAspectRatio="none">
    <polygon points="0,0 54,0 0,36" fill="var(--navy)"/>
    <polygon points="0,238 140,366 0,366" fill="#dfe0e5"/>
    <polygon points="140,305 259,305 259,366 220,366" fill="#ecebe6"/>
  </svg>
  <div class="abs intro-kicker">PROPOSAL FOR</div>
  <h2 class="abs intro-title">OUTSOURCED CFO<br>SERVICES</h2>
  <div class="abs intro-meta">
    <div class="lab">PREPARED FOR</div>
    <div class="client">Abc Limited</div>
    <div class="by">BY</div>
    <div class="who">Owen Harcourt, Director, Thornvale Advisory</div>
    <div class="note">Owen Harcourt will be the Thornvale Advisory Director responsible for your affairs. Should Owen not be available, your alternate contact will be Clara Venti.</div>
  </div>
  <div class="head-card" style="left:24px;top:182px"><div class="portrait" role="img" aria-label="Portrait of Owen Harcourt"></div><div class="tag">OWEN HARCOURT</div></div>
  <div class="head-card" style="left:146px;top:182px"><div class="portrait" role="img" aria-label="Portrait of Clara Venti"></div><div class="tag">CLARA VENTI</div></div>
  <div class="head-bio" style="left:24px;top:243px">
    <h4>Owen Harcourt, CA, CTA, Director</h4>
    <p>Owen has been a Chartered Accountant for 20 years. He specialises in complex tax matters, international tax and business valuations.</p>
    <p>Owen advises a number of significant clients, including Australia's third largest privately held technology company.</p>
  </div>
  <div class="head-bio" style="left:146px;top:243px">
    <h4>Clara Venti, CA, Director<br>Financial Reporting and CFO Services</h4>
    <p>Clara has been a Chartered Accountant for 20 years and manages a portfolio of corporate clients.</p>
    <p>She provides strategic advice, outsourced CFO and tax services to ASX Listed Companies.</p>
  </div>
</section>

<!-- 5 · Letter -->
<section class="page p-letter">
  <svg class="shapes" viewBox="0 0 259 366" preserveAspectRatio="none">
    <polygon points="60,0 259,0 259,120" fill="#f4f3ef"/>
    <polygon points="0,290 120,366 0,366" fill="#e2e3e8"/>
    <polygon points="259,335 259,366 212,366" fill="var(--gold)"/>
  </svg>
  <div class="abs wordmark" style="left:23px;top:40px;font-size:7px"><span class="mark"></span>Thornvale Advisory</div>
  <div class="abs letter-rule"></div>
  <div class="abs letter-body small">
    <p>22 April 2025</p>
    <p>[insert name]<br>[insert company name]<br>Via email:</p>
    <p>Dear [salutation],</p>
    <p>PROPOSAL FOR ADVISORY SERVICES</p>
    <p>We are delighted to submit our proposal to Skyline Group for the provision of advisory services. Based on our discussions with you we have been asked to provide the following proposal:</p>
    <p>Our main objective is to provide you with:</p>
    <ul class="dash" style="margin-bottom:5.9px">
      <li>An independent review of your business forecasts and plans using Ledgerly data and Cashwise Predict software to assist with making business decisions with confidence</li>
      <li>Comfort &amp; certainty to allow you to reward/draw an appropriate dividend based on the forecasted future cashflows of the business (3 months of expenses kept in cash)</li>
      <li>We will do this by working with Helen and using Cashwise Predict cashflow forecasting tool and providing you reports and meetings on an agreed schedule.</li>
    </ul>
    <p style="margin-bottom:0">Our scope includes:</p>
    <ul class="dash" style="margin-bottom:5.9px">
      <li>Initial needs analysis and client "deep dive," including understanding and incorporating your current tools and plans into the software package.</li>
      <li>Cashwise configuration and Ledgerly linking, (including input of budgets and forecasts prepared internally). Including calls and meetings as required.</li>
      <li>Provision of training to Helen in Cashwise Product.</li>
      <li>Quarterly Cashflow forecast reports to be provided, with alternative scenarios available.</li>
      <li>Quarterly meetings (F2F or video call) to discuss the reports.</li>
      <li>All calls/emails in respect of the project (except where part of agreed out of scope services)</li>
    </ul>
    <p style="margin-bottom:0">Agreed out of scope services include:</p>
    <ul class="dash">
      <li>Bookkeeping or data input and reconciliation services (Helen responsibility)</li>
      <li>Tax and accountancy services provided under our earlier engagement letter</li>
      <li>Additional meetings, additional scenarios or adjustments requested after meetings and subsequent reissuance of reports</li>
    </ul>
  </div>
</section>

<!-- 6 · Fees -->
<section class="page p-fees">
  <svg class="shapes" viewBox="0 0 259 366" preserveAspectRatio="none">
    <polygon points="40,0 259,0 259,140" fill="#f4f3ef"/>
  </svg>
  <div class="abs fees-body small">
    <p style="margin-top:0">Below is our estimated fee given our conversations</p>
    <table class="fee-table">
      <tr><th style="width:38%">Task</th><th style="width:18%">Number per year</th><th class="num" style="width:22%">Cost per Quarter (ex-GST)</th><th class="num">Estimated Annual Cost (Ex GST)</th></tr>
      <tr><td>Preparation of Reports and discussions with Helen/Skyline</td><td class="num">4</td><td class="num">$1,302.50</td><td class="num">$5,210.00</td></tr>
      <tr><td>Quarterly Meetings</td><td class="num">4</td><td class="num">$995.50</td><td class="num">$3,982.00</td></tr>
      <tr><td>KPI Review</td><td class="num">4</td><td class="num">$452.00</td><td class="num">$1,808.00</td></tr>
      <tr class="gap"><td></td><td></td><td></td><td></td></tr>
      <tr class="total"><td>Total</td><td></td><td class="num">$2,750.00</td><td class="num">$11,000.00</td></tr>
      <tr class="gap"><td colspan="4"></td></tr>
      <tr><td colspan="4">In addition to the quarterly reports there will be a one-off setup and configuration charge as listed in scope above which will also include training to Helen as appropriate</td></tr>
      <tr class="gap"><td colspan="4"></td></tr>
      <tr class="total"><td>Estimated setup costs</td><td class="num">1</td><td></td><td class="num">$2,500.00-$3,500.00</td></tr>
    </table>
    <p>Our costs will be reviewed annually to ensure the fee is appropriate to the level of service required.</p>
    <p>It is our expectation that in the initial stages of our engagement, our time inputs will be higher than the long-term average that we have based our quote upon. We consider this our investment in the ongoing relationship as we work to understand your business and build best practice processes. We will endeavour to avoid out of scope charges to you as much as possible</p>
    <p>In acknowledgment of our learning curve, we respectfully request a minimum 6 month engagement. We have no doubt that at the end of the year you will be delighted with the service we have provided.</p>
    <p style="margin-bottom:6px">The table below provides an indication of our team and their hourly rates should you request additional services.</p>
    <table class="rate-table">
      <tr><th>Level of Expertise</th><th class="num">Hourly Rates (Ex GST)</th></tr>
      <tr><td>Associate Director/Director</td><td class="num">$350 - $515 Per hour</td></tr>
      <tr><td>Supervisor/Manager</td><td class="num">$225 – $315 per hour</td></tr>
      <tr><td>Senior Accountant</td><td class="num">$180 - $225 per hour</td></tr>
      <tr><td>Intermediate Accountant</td><td class="num">$120 – $180 per hour</td></tr>
      <tr><td>Bookkeeper</td><td class="num">$80 per hour</td></tr>
      <tr><td>Administration</td><td class="num">$80 - $95 per hour</td></tr>
      <tr><td>Accounting Cadette</td><td class="num">$70 per hour</td></tr>
    </table>
  </div>
</section>

<!-- 7 · Closing -->
<section class="page p-closing">
  <div class="photo" style="left:0;top:170px;width:259px;height:196px;background:linear-gradient(#fff 0%,#dcdde2 30%,#c9c4c2 52%,#d8a98a 66%,#6f7a86 78%,#4d5a66 100%)" role="img" aria-label="Photo of a harbour bridge and waterfront at sunset"></div>
  <div class="abs closing-body small">
    <p>Should you have any queries or wish to discuss, please do not hesitate to contact me or Clara on telephone (02) 9000 4100 or email clara@thornvale.net.au.</p>
    <p>Yours sincerely,</p>
    <p class="closing-sign">Owen Harcourt<br>Director</p>
  </div>
</section>

<!-- 8 · Acceptance -->
<section class="page p-accept">
  <svg class="shapes" viewBox="0 0 259 366" preserveAspectRatio="none">
    <polygon points="0,270 165,334 259,296 259,366 0,366" fill="var(--navy)"/>
    <polygon points="259,262 259,366 148,366" fill="var(--cream)"/>
    <polygon points="259,272 259,366 163,366" fill="var(--gold)"/>
  </svg>
  <div class="abs accept-body">
    <h3>Acceptance</h3>
    <p class="small" style="margin-bottom:15px">I have read this proposal and I am pleased to accept the terms and conditions set out herein and attached.</p>
    <div class="accept-list">
      <div class="hd">CFO Services</div><div class="hd">Accepted</div>
      <div>Onboarding</div><div><span class="box"></span></div>
      <div>Weekly meetings</div><div><span class="box"></span></div>
      <div>Monthly meetings</div><div><span class="box"></span></div>
      <div>Appendix 4D</div><div><span class="box"></span></div>
      <div>Appendix 4E</div><div><span class="box"></span></div>
      <div>Audit committee meetings</div><div><span class="box"></span></div>
      <div>Ad-hoc attendances</div><div><span class="box"></span></div>
      <div class="hd" style="margin-top:10px">Payroll Services</div><div class="hd" style="margin-top:10px">Accepted</div>
      <div>Weekly payroll</div><div><span class="box"></span></div>
      <div>Monthly payroll</div><div><span class="box"></span></div>
    </div>
    <div class="sign-grid">
      <div>Signed:</div><div></div><div></div>
      <div>Name:</div><div><div class="dots"></div>Director</div><div><div class="dots"></div>Director</div>
      <div>Date:</div><div><div class="dots"></div></div><div><div class="dots"></div></div>
    </div>
    <p class="small" style="margin-top:12px">On acceptance we will send you our engagement letter.</p>
  </div>
  <div class="abs liability">Liability limited by a scheme<br>approved under Professional<br>Standards Legislation.</div>
  <div class="abs wordmark accept-brand"><span class="mark"></span>Thornvale Advisory</div>
</section>

</body>
</html>
```